Criação de Papelaria (6 itens) para Arquitetura
" Sou recém formada em Design de Interiores e pretendo começar a divulgar meu negócio. Já fiz alguns trabalhos / projetos, mas ainda não consegui alavancar minha marca. Meu foco será a realização de projetos residenciais, comerciais e empresariais. As atividades vão desde a entrevista inicial para entendimento das necessidades do cliente, passando pela preparação dos projetos com imagens renderizadas, plantas baixas, projetos de marcenaria, iluminação, gesso etc., incluindo também acompanhamento a lojas para escolha de materiais / móveis até o acompanhamento da obra e fiscalização dos trabalhos executados por terceiros. "

```html
<!DOCTYPE html>
<html lang="pt-BR">
<head>
<meta charset="UTF-8">
<title>Lia Moreira — Cartão de Visita</title>
<link rel="stylesheet" href="https://fonts.googleapis.com/css2?family=Raleway:wght@300;400;700&display=swap">
<style>
  :root{
    --page:#e6e4e8;
    --plum:#4a4559;
    --plum-deep:#3d3849;
    --rose-gold:#e1a996;
    --rose-gold-light:#f2c7b8;
    --blush:#fbeeee;
    --paper:#ffffff;
    --ink:#3b3a40;
    --ink-soft:#6f6c75;
    --icon:#5a5662;
    --logo-light:#dcd8e2;
    --rule:#b9b5bd;
  }
  *{margin:0;padding:0;box-sizing:border-box;}
  html,body{width:1200px;height:1200px;overflow:hidden;}
  body{
    background:var(--page);
    font-family:"Raleway",sans-serif;
    display:flex;flex-direction:column;align-items:center;justify-content:center;gap:80px;
  }
  .card{
    position:relative;width:820px;height:455px;border-radius:28px;overflow:hidden;
    box-shadow:0 10px 30px rgba(40,30,50,.18);
  }

  /* Front */
  .card--front{background:linear-gradient(135deg,var(--plum) 0%,var(--plum-deep) 100%);}
  .front__band-vertical{
    position:absolute;left:62px;top:0;bottom:0;width:5px;
    background:linear-gradient(180deg,var(--rose-gold-light),var(--rose-gold));
  }
  .front__band-horizontal{
    position:absolute;left:0;right:0;top:360px;height:4px;
    background:linear-gradient(90deg,var(--rose-gold),var(--rose-gold-light));
  }
  .front__brand{
    position:absolute;left:0;right:0;top:118px;
    display:flex;flex-direction:column;align-items:center;gap:26px;
  }
  .brand__square{width:66px;height:66px;background:var(--rose-gold);}
  .front__name{
    font-weight:300;font-size:58px;letter-spacing:10px;color:var(--logo-light);text-transform:uppercase;
  }

  /* Back */
  .card--back{background:linear-gradient(120deg,var(--paper) 0%,var(--blush) 100%);}
  .back__rule{
    position:absolute;left:0;right:0;height:0;border-top:2px dotted var(--rule);
  }
  .back__rule--top{top:26px;}
  .back__rule--bottom{bottom:26px;}
  .back__identity{position:absolute;left:60px;top:66px;}
  .identity__name{font-weight:700;font-size:30px;color:var(--ink);}
  .identity__role{font-size:18px;color:var(--ink-soft);margin-top:4px;}
  .contact-list{position:absolute;left:60px;top:170px;list-style:none;display:flex;flex-direction:column;gap:22px;}
  .contact-item{display:flex;align-items:center;gap:16px;font-size:15px;color:var(--ink-soft);line-height:1.35;}
  .contact-icon{width:34px;height:34px;border-radius:50%;background:var(--icon);flex:none;display:flex;align-items:center;justify-content:center;}
  .contact-icon svg{width:18px;height:18px;}
  .back__brand{
    position:absolute;right:70px;top:150px;display:flex;flex-direction:column;align-items:center;gap:18px;
  }
  .back__brand .brand__square{width:80px;height:80px;background:var(--rose-gold-light);opacity:.75;}
  .back__name{font-weight:300;font-size:46px;letter-spacing:7px;color:var(--rose-gold);text-transform:uppercase;}
  .back__tagline{font-weight:400;font-size:14px;letter-spacing:6px;color:var(--rose-gold);text-transform:uppercase;margin-top:-10px;}
</style>
</head>
<body>

  <section class="card card--front" aria-label="Frente do cartão">
    <div class="front__band-vertical"></div>
    <div class="front__band-horizontal"></div>
    <div class="front__brand">
      <div class="brand__square"></div>
      <div class="front__name">Lia Moreira</div>
    </div>
  </section>

  <section class="card card--back" aria-label="Verso do cartão">
    <div class="back__rule back__rule--top"></div>
    <div class="back__rule back__rule--bottom"></div>

    <div class="back__identity">
      <div class="identity__name">Nome Completo</div>
      <div class="identity__role">Cargo</div>
    </div>

    <ul class="contact-list">
      <li class="contact-item">
        <span class="contact-icon">
          <svg viewBox="0 0 24 24" fill="#fff"><path d="M6.6 10.8a15 15 0 0 0 6.6 6.6l2.2-2.2c.3-.3.7-.4 1-.2 1.1.4 2.3.6 3.6.6.6 0 1 .4 1 1V20c0 .6-.4 1-1 1A17 17 0 0 1 3 4c0-.6.4-1 1-1h3.5c.6 0 1 .4 1 1 0 1.3.2 2.5.6 3.6.1.3 0 .7-.2 1z"/></svg>
        </span>
        <span>(11) 0000-0000<br>(11) 0000-0000</span>
      </li>
      <li class="contact-item">
        <span class="contact-icon">
          <svg viewBox="0 0 24 24" fill="none" stroke="#fff" stroke-width="2"><rect x="3" y="6" width="18" height="12" rx="1"/><path d="M3 7l9 6 9-6"/></svg>
        </span>
        <span>www.liamoreira.com.br<br>contato@liamoreira.com.br</span>
      </li>
      <li class="contact-item">
        <span class="contact-icon">
          <svg viewBox="0 0 24 24" fill="#fff"><path d="M12 2a7 7 0 0 0-7 7c0 5 7 13 7 13s7-8 7-13a7 7 0 0 0-7-7zm0 9.5A2.5 2.5 0 1 1 12 6.5a2.5 2.5 0 0 1 0 5z"/></svg>
        </span>
        <span>Lia Moreira Design<br>Rua: Seu Endereço - Bairro<br>Cidade - SP - CEP 0000-000</span>
      </li>
    </ul>

    <div class="back__brand">
      <div class="brand__square"></div>
      <div class="back__name">Lia Moreira</div>
      <div class="back__tagline">Design de Interiores</div>
    </div>
  </section>

</body>
</html>
```